3D visuals for homeowners planning a building project, visuals show how house would look...

I offer excellent quality 3D visuals of how home would look after building project or renovation has been completed.
A5 double sided please,

I would not like to influence you too much but I thought that flyer could for exemple show "before...and after"
(like regrowing someone`s hair :-)))

where "before" would be a boring black/white drawing (uploaded), and "after" - the superb 3D visual etc...

front side could be this building project - kitchen extension and back side coud be bathroom,

again - its just an idea, I actually submitted the project to MakerHive as I dont trust too much my own judgment :-)

I hope someone has better idea !!!

Target Market(s)

Homeowners planning a building project

Industry/Entity Type

Graphic Art

Requirements
Must have
• I offer 3D home visuals.
• Excellent detailed quality.
• Only £32 per image.
• Tel : 07700900418
• email : quillbeam@mernova.net

```html
<!DOCTYPE html>
<html lang="en">
<head>
<meta charset="utf-8">
<title>3D Home Visuals Flyer</title>
<link href="https://fonts.googleapis.com/css2?family=Arimo:wght@400;700&display=swap" rel="stylesheet">
<style>
  :root {
    --maroon: #7a1e2c;
    --tan-light: #e3c9a0;
    --tan-dark: #b98f5e;
    --yellow: #ffe500;
    --ink: #1f1a17;
    --white: #ffffff;
    --frame: #f4f1ec;
  }
  html, body { margin: 0; padding: 0; overflow: hidden; }
  body { width: 900px; height: 1200px; background: var(--maroon); font-family: "Arimo", Arial, sans-serif; }
  .flyer { position: relative; width: 900px; height: 1200px; background: var(--maroon); overflow: hidden; }
  .web-address { position: absolute; top: 38px; right: 40px; color: var(--white); font-size: 19px; }
  .company-name { position: absolute; top: 112px; left: 0; width: 100%; margin: 0; text-align: center; color: var(--white); font-size: 52px; font-weight: 700; letter-spacing: 0.5px; }
  .showcase { position: absolute; top: 215px; left: 0; width: 900px; height: 765px; background: linear-gradient(180deg, var(--tan-light) 0%, var(--tan-dark) 100%); }
  .visual { position: absolute; border: 9px solid var(--frame); box-shadow: 0 6px 14px rgba(0,0,0,0.35); }
  .visual-main { top: 30px; left: 140px; width: 670px; height: 385px; background: linear-gradient(160deg, #e9eaec 0%, #c9cbce 45%, #4a3a30 70%, #6f8e4e 100%); }
  .visual-bathroom { top: 455px; left: 36px; width: 396px; height: 280px; background: linear-gradient(150deg, #f1efea 0%, #d9d3c7 50%, #6b5a48 100%); }
  .visual-kitchen { top: 455px; left: 470px; width: 394px; height: 280px; background: linear-gradient(150deg, #eceeef 0%, #b8bcbf 50%, #a0703f 100%); }
  .service-label { position: absolute; top: 8px; left: 195px; width: 420px; height: 56px; background: var(--yellow); color: var(--ink); font-size: 32px; font-weight: 700; display: flex; align-items: center; justify-content: center; z-index: 2; }
  .price-badge { position: absolute; width: 74px; height: 74px; border-radius: 50%; background: var(--yellow); color: var(--ink); font-size: 27px; font-weight: 700; display: flex; align-items: center; justify-content: center; z-index: 3; }
  .badge-main { top: 375px; left: 760px; }
  .badge-bathroom { top: 705px; left: 18px; }
  .badge-kitchen { top: 705px; left: 492px; }
  .price-band { position: absolute; top: 1005px; left: 36px; width: 828px; height: 66px; background: var(--yellow); color: var(--ink); font-size: 44px; display: flex; align-items: center; justify-content: center; }
  .contact { position: absolute; left: 325px; top: 1095px; color: var(--white); font-size: 27px; }
  .contact-line { display: flex; align-items: center; height: 44px; }
  .contact-line svg { width: 30px; height: 26px; margin-right: 26px; }
</style>
</head>
<body>
<div class="flyer">
  <div class="web-address">www.quillbeamvisuals.com</div>
  <h1 class="company-name">YOUR COMPANY NAME</h1>

  <section class="showcase">
    <div class="service-label">3D home visuals</div>
    <div class="visual visual-main" role="img" aria-label="3D visual of a house with a rear extension and roof lights"></div>
    <div class="price-badge badge-main">£32</div>

    <div class="visual visual-bathroom" role="img" aria-label="3D visual of a bathroom with vanity unit and bath"></div>
    <div class="price-badge badge-bathroom">£32</div>

    <div class="visual visual-kitchen" role="img" aria-label="3D visual of a kitchen with island and wooden floor"></div>
    <div class="price-badge badge-kitchen">£32</div>
  </section>

  <div class="price-band">£32 per image</div>

  <div class="contact">
    <div class="contact-line">
      <svg viewBox="0 0 30 26" aria-hidden="true">
        <path d="M2 8 Q15 -1 28 8 L24 12 L20 8 L10 8 L6 12 Z" fill="var(--white)"/>
        <rect x="6" y="13" width="18" height="11" rx="2" fill="var(--white)"/>
        <circle cx="15" cy="18.5" r="3" fill="var(--maroon)"/>
      </svg>
      <span>07700900418</span>
    </div>
    <div class="contact-line">
      <svg viewBox="0 0 30 26" aria-hidden="true">
        <rect x="2" y="4" width="26" height="18" fill="none" stroke="var(--white)" stroke-width="2"/>
        <path d="M2 4 L15 15 L28 4" fill="none" stroke="var(--white)" stroke-width="2"/>
      </svg>
      <span>quillbeam@mernova.net</span>
    </div>
  </div>
</div>
</body>
</html>
```